Home based bath & shave business wants to redesign labels

I would like to have new labels designed to fit the body lotion and bath oil bottles. We want them similar but different. The key ingredient for all of Ferrante's Bath & Shave products is olive oil.

You are free to change colors. I have attached our logo and current labels. The current labels just don't look right to me (pictures attached). I like the script font, but am willing to entertain another. I have our logo in several formats and the font, should you want it.

Target Market(s)

Women

Industry/Entity Type

Business

Font styles to use
Decorative
Script

Requirements
Must have
• Both product labels must include our logo.The logo must stay the same though to make it work with the label, you can change the color if needed.
• It should be a vertical label.
• The bottle used is a 8 oz Clear PET Tapered Naples Oval Bottle (I have attached pictures) and its dimensions are:
• Length 2.548 in / 6.472 cm
• Width 1.479 in / 3.757 cm
• Height 6.639 in / 16.863 cm

```html
<!DOCTYPE html>
<html lang="en">
<head>
<meta charset="utf-8">
<title>Ferrante's Bath &amp; Shave – Labels</title>
<link rel="stylesheet" href="https://fonts.googleapis.com/css2?family=Great+Vibes&family=Open+Sans:wght@400;700&display=swap">
<style>
  :root {
    --page: #ffffff;
    --frame: #f7a21b;
    --tab: #ffffff;
    --brand-red: #e8342a;
    --lotion-pink: #ec63b4;
    --lotion-pink-dark: #e04fa6;
    --cream: #f3ece0;
    --cream-dark: #e3d6c1;
    --olive: #5c7a1c;
    --oil-green-light: #b8dc52;
    --oil-green: #7fb32c;
    --oil-green-dark: #3f7a18;
    --olive-purple: #6a3a4e;
    --title: #ffffff;
    --ingredient-red: #e0343f;
    --ingredient-white: #ffffff;
  }
  html, body { margin: 0; padding: 0; overflow: hidden; }
  body { width: 1200px; height: 1000px; background: var(--page); position: relative; }

  .label {
    position: absolute; top: 93px; height: 814px; width: 443px;
    box-sizing: border-box; border: 5px solid var(--frame); border-radius: 4px;
    overflow: hidden;
  }
  .label--lotion { left: 85px; background: var(--lotion-pink); }
  .label--oil { left: 638px; width: 445px; }

  .label__photo { position: absolute; inset: 0; }
  .label--lotion .label__photo { inset: auto 0 0 0; height: 400px; }

  .brand-tab {
    position: absolute; top: -5px; width: 314px; height: 235px;
    box-sizing: border-box; background: var(--tab);
    border: 5px solid var(--frame); border-top: none;
    border-radius: 0 0 70px 70px;
    display: flex; align-items: center; justify-content: center;
  }
  .label--lotion .brand-tab { left: 58px; }
  .label--oil .brand-tab { left: 62px; }
  .brand-tab__name {
    font-family: "Open Sans", sans-serif; font-weight: 700;
    color: var(--brand-red); font-size: 27px; line-height: 1.2;
    text-align: center; margin: 0;
  }

  .product-title {
    position: absolute; left: 0; right: 0; top: 255px; height: 190px;
  }
  .product-title svg { position: absolute; inset: 0; }
  .product-title__text {
    position: absolute; left: 0; right: 0; top: 50px; margin: 0;
    text-align: center; font-family: "Great Vibes", cursive; font-weight: 400;
    font-size: 78px; color: var(--title); line-height: 1;
    text-shadow: 0 0 2px rgba(60,40,40,.55);
  }

  .ingredients {
    position: absolute; left: 30px; right: 30px; margin: 0;
    font-family: "Open Sans", sans-serif; text-align: center;
  }
  .label--lotion .ingredients {
    bottom: 18px; font-size: 10.5px; line-height: 1.45; color: var(--ingredient-red);
  }
  .label--oil .ingredients {
    bottom: 22px; font-size: 14px; color: var(--ingredient-white);
    text-shadow: 0 1px 2px rgba(0,0,0,.5);
  }
</style>
</head>
<body>

<section class="label label--lotion">
  <svg class="label__photo" viewBox="0 0 433 400" preserveAspectRatio="none" role="img" aria-label="Photo of a creamy milk splash with olives and olive oil">
    <defs>
      <linearGradient id="lotion-splash" x1="0" y1="0" x2="0" y2="1">
        <stop offset="0" stop-color="var(--cream-dark)"/>
        <stop offset="0.45" stop-color="var(--cream)"/>
        <stop offset="1" stop-color="var(--cream)"/>
      </linearGradient>
    </defs>
    <path d="M0 20 C60 60 120 110 200 140 C290 170 360 185 433 180 L433 400 L0 400 Z" fill="url(#lotion-splash)"/>
  </svg>

  <header class="brand-tab">
    <p class="brand-tab__name">Ferrante's<br>Bath &amp; Shave</p>
  </header>

  <div class="product-title">
    <svg viewBox="0 0 433 190" aria-hidden="true">
      <path d="M40 50 Q216 10 393 50" fill="none" stroke="#fff" stroke-width="2"/>
      <path d="M45 170 L200 170 M233 170 L388 170" stroke="#fff" stroke-width="2"/>
      <rect x="210" y="163" width="12" height="12" transform="rotate(45 216 169)" fill="none" stroke="#fff" stroke-width="2"/>
    </svg>
    <h1 class="product-title__text">Body Lotion</h1>
  </div>

  <p class="ingredients">Ingredients: Water, Olive Oil, Aloe Vera Juice, Avocado Oil, Rice Bran Oil, BTMS-50, Glycerin, Stearyl Alchohol, Oat Extract, DL Panthenol, Preservix, Buckthorn Extract, Vitamin E and Fragrance oil</p>
</section>

<section class="label label--oil">
  <svg class="label__photo" viewBox="0 0 435 804" preserveAspectRatio="none" role="img" aria-label="Photo of olive branches with green leaves above a pile of ripe olives">
    <defs>
      <radialGradient id="oil-leaves" cx="0.5" cy="0.3" r="0.8">
        <stop offset="0" stop-color="var(--oil-green-light)"/>
        <stop offset="0.6" stop-color="var(--oil-green)"/>
        <stop offset="1" stop-color="var(--oil-green-dark)"/>
      </radialGradient>
      <linearGradient id="oil-olives" x1="0" y1="0" x2="1" y2="0">
        <stop offset="0" stop-color="var(--olive)"/>
        <stop offset="0.5" stop-color="var(--olive-purple)"/>
        <stop offset="1" stop-color="var(--olive)"/>
      </linearGradient>
    </defs>
    <rect width="435" height="804" fill="url(#oil-leaves)"/>
    <path d="M0 700 Q100 660 220 680 T435 670 L435 804 L0 804 Z" fill="url(#oil-olives)"/>
  </svg>

  <header class="brand-tab">
    <p class="brand-tab__name">Ferrante's<br>Bath &amp; Shave</p>
  </header>

  <div class="product-title">
    <svg viewBox="0 0 435 190" aria-hidden="true">
      <path d="M40 50 Q217 10 395 50" fill="none" stroke="#fff" stroke-width="2"/>
      <path d="M45 170 L201 170 M234 170 L390 170" stroke="#fff" stroke-width="2"/>
      <rect x="211" y="163" width="12" height="12" transform="rotate(45 217 169)" fill="none" stroke="#fff" stroke-width="2"/>
    </svg>
    <h1 class="product-title__text">Bath Oil</h1>
  </div>

  <p class="ingredients">Ingredients: olive oil, Grapeseed oil and fragrance oil.</p>
</section>

</body>
</html>
```